Flyer Design Project for Brightwater Wellbeing Rooms

We are a psychology clinic that specialises in eating, parenting and chronic illness & pain. See our website for a summary.

We need a flyer that will go to doctors and schools in the local area.

Things to include on the front page:

Immediate appointments available
After hours appointments available
Male and female psychologists

Phone 9563 2190
Web brightwaterwellbeingrooms.com.au

On the back page:

Phone 9563 2190
Suite 1/1287 Marlowe Rd, Kelverton East 3185.
brightwaterwellbeingrooms.com.au

Parenting: Parenthood is an amazing journey, but for lots of people it raises all sorts of issues from fear of birth, breastfeeding difficulties and settling problems, to toddler discipline and food fussiness all the way through to getting help for your depressed or anxious adolescent. Our Parenting Psychologists can help you be the best parent you can be which will in turn lead to happier families, homes, children and parents.

Chronic illness/pain: Diabetes, heart disease, arthritis, asthma, migraines, dizziness, chronic fatigue syndrome, infertility, and PCOS are just some of the conditions that can be managed with psychological interventions. Everything we do is about helping you to manage your condition and get back to focusing on what you really want your life to be about.

Eating: Whether you suffer from anorexia, bulimia or binge eating, our strategies help you develop a healthy relationship with food and your body. The practical tips and strategies that we can provide are very useful for people undergoing lapband surgery or liposuction.

I am interested in whether the photographs that I have already purchased can be used...so please have a look through the website and see which you think will suit your design. Photographs are not absolutely necessary though, so if it doesn't fit with your idea that is okay too.
Updates

HI Everyone,

Thanks for submitting so far! I haven't found anything yet that has hit the mark. And I am thinking that is my fault and maybe that way i have described what I want. I apologise and hope that this update might help.

This brochure is likely to sit with lots of other brochures in a doctors waiting room so it needs to be different - so that it will be noticed.

The majority of our market are women - so something feminine is important. Maybe it needs to be a little more playful that I had initially thought. Like maybe not your standard blocky text and bolds and primary colours. But something more creative, more personal.

I want to not focus just on the family theme. Parenting is one area that we cover, but also we help people with eating disorders and chronic illness/chronic pain. So the photographs that I use need to be more general. It is importnat to focus on happy and healthy looking people. As we went to appeal to what my potential clients want to look like and feel like.

I do hope this helps to guide you. I promise that once I see a flyer that I could choose, I will turn the funding to guaranteed. I did this last time...I am just a bit nervous as I haven't received anything yet that I am excited about.

Kindest regards,

Marnie.

Hi Everyone,

Thank you for your designs coming in! As promised, as soon as I received a design that I could see myself choosing I would change the status from refundable to committed. I have now done this!

I have received a design that I would say is good. It is not perfect however...so please keep the ideas coming.

To give more direction, the one that came in has a nice theme that runs through the brochure. Not too many different types of font and colours detracting from the flow of the flyer. However, the thing that I am concerned about is whether it will stand out enough on a rack of other flyers in a doctors waiting room.

I hope this helps with your creative ideas.

Thanks again to everyone!

Marnie.

Thanks SO much to everyone who is putting in designs. You are making my decision difficult!

I am wondering if you can update your designs with a few things:

can I ask you to make some text changes:

1. Can we have a heading on the front page: Psychologists  and then can you put Kelverton East in smaller writing just below it?

2. Id like to say on the front: Specialising in parenting, disordered eating and chronic pain & illness

3. Delete Male & Female Psychologists

4. In general we dont' need to have the logo standing out. We don't have a well known brand yet, so I am not wanting to take up valuable space with this - so perhaps it shoudl be small and maybe just on the back? Keeping the name of our clinic on the front with the website shoudl be sufficient.

Thanks heaps everyone...I will make decision very soon!

Target Market(s)

20-40 year olds. Working. Educated. Female. They might have a family/children.
Australian. Engish speaking.

Industry/Entity Type

Clinic

Requirements
Must have
• I would like to include our logo. Please do not use the colour green that it is in. I hate that colour! but I LOVE the logo.

I would like to follow through with some of the themes of the website and other stationary.

I will attach some of the other stationary I have had designed.

I really like the colours in the letterhead - especially that blue of the logo.

I think it needs to have a dash of colour with it at least...something that will stand out and be noticed on a brochure rack...but also have a look of class/sophistication/modern.
Nice to have
• Perhaps photograph of happy and healthy people.
Should not have
• I don't like bold text or too many different types of fonts.

It shouldn't look too cluttered so I might need to reduce the text I have included - I will need to see it first.

```html
<!DOCTYPE html>
<html lang="en">
<head>
<meta charset="utf-8">
<title>Brightwater Wellbeing Rooms – Flyer</title>
<link rel="stylesheet" href="https://fonts.googleapis.com/css2?family=PT+Sans:wght@400;700&family=Roboto+Condensed:wght@700&family=Cormorant+Garamond:wght@500&display=swap">
<style>
  :root {
    --page: #ffffff;
    --grey-light: #f2f2f2;
    --grey-mid: #d4d4d4;
    --green-pale: #eef8c4;
    --green-mid: #d6ec96;
    --green-deep: #b9d86a;
    --green-rim: #cfe98a;
    --grass-light: #cfe2a0;
    --grass-deep: #6e9d36;
    --brown: #6a2c0c;
    --body-text: #2a2a2a;
    --sky: #47b9e6;
    --aqua: #3fcfdc;
    --address-blue: #2f8fd8;
    --logo-grey: #6f6f6f;
    --logo-teal: #9fe0d6;
  }
  * { box-sizing: border-box; margin: 0; padding: 0; }
  html, body { width: 1200px; height: 1200px; overflow: hidden; background: var(--page); }
  .canvas { position: relative; width: 1200px; height: 1200px; background: var(--page); }

  .panel {
    position: absolute; top: 55px; width: 506px; height: 1063px; overflow: hidden;
    box-shadow: 4px 5px 8px rgba(0,0,0,0.35);
  }
  .panel--front { left: 67px; }
  .panel--back { left: 620px; }
  .panel-bg { position: absolute; inset: 0; width: 100%; height: 100%; }

  .brand-mark { position: absolute; display: flex; align-items: center; gap: 14px; }
  .brand-mark__dot { border-radius: 50%; background: var(--logo-teal); flex: none; }
  .brand-mark__name {
    font-family: "PT Sans", sans-serif; font-weight: 400; color: var(--logo-grey);
    text-transform: uppercase; letter-spacing: 3px;
  }
  .panel--front .brand-mark { left: 22px; top: 30px; }
  .panel--front .brand-mark__dot { width: 62px; height: 62px; }
  .panel--front .brand-mark__name { font-size: 19px; line-height: 29px; }

  .features { position: absolute; right: 26px; top: 212px; list-style: none; text-align: right; }
  .features li {
    font-family: "Cormorant Garamond", serif; font-weight: 500; font-size: 35px;
    color: var(--sky); line-height: 40px; margin-bottom: 39px;
    display: flex; justify-content: flex-end; align-items: center; gap: 6px; white-space: nowrap;
  }
  .features svg { width: 26px; height: 26px; flex: none; }

  .front-phone {
    position: absolute; left: 26px; right: 20px; top: 440px;
    font-family: "Roboto Condensed", sans-serif; font-weight: 700; font-size: 38px;
    color: var(--brown); letter-spacing: -0.6px; white-space: nowrap;
  }
  .front-web {
    position: absolute; left: 26px; top: 508px;
    font-family: "Cormorant Garamond", serif; font-weight: 500; font-size: 26px;
    color: var(--brown); white-space: nowrap;
  }

  .services {
    position: absolute; left: 25px; width: 465px; top: 8px;
    font-family: "PT Sans", sans-serif; font-size: 18px; line-height: 26px;
    color: var(--body-text); text-align: justify;
  }
  .services p { margin-bottom: 26px; }
  .services .service-title { font-weight: 700; font-size: 24px; color: var(--brown); }

  .panel--back .brand-mark { left: 145px; top: 778px; gap: 14px; }
  .panel--back .brand-mark__dot { width: 56px; height: 56px; }
  .panel--back .brand-mark__name { font-size: 16px; line-height: 23px; }

  .address {
    position: absolute; left: 0; right: 0; top: 862px; text-align: center; font-style: normal;
    font-family: "PT Sans", sans-serif; font-size: 21px; line-height: 32px; color: var(--address-blue);
  }
  .back-phone {
    position: absolute; left: 0; right: 0; top: 982px; text-align: center;
    font-family: "Roboto Condensed", sans-serif; font-weight: 700; font-size: 40px;
    color: var(--aqua); letter-spacing: -0.5px; white-space: nowrap;
  }
</style>
</head>
<body>
<main class="canvas">

  <section class="panel panel--front">
    <svg class="panel-bg" viewBox="0 0 506 1063" preserveAspectRatio="none" aria-hidden="true">
      <defs>
        <linearGradient id="frontGrey" x1="0" y1="0" x2="1" y2="1">
          <stop offset="0" stop-color="var(--grey-mid)"/>
          <stop offset="0.5" stop-color="var(--grey-light)"/>
          <stop offset="1" stop-color="var(--grey-mid)"/>
        </linearGradient>
        <linearGradient id="frontGreen" x1="0" y1="0" x2="0.3" y2="1">
          <stop offset="0" stop-color="var(--green-pale)"/>
          <stop offset="0.6" stop-color="var(--green-mid)"/>
          <stop offset="1" stop-color="var(--green-deep)"/>
        </linearGradient>
        <linearGradient id="grass" x1="0" y1="0" x2="0" y2="1">
          <stop offset="0" stop-color="var(--green-mid)"/>
          <stop offset="0.25" stop-color="var(--grass-light)"/>
          <stop offset="1" stop-color="var(--grass-deep)"/>
        </linearGradient>
      </defs>
      <rect width="506" height="1063" fill="url(#frontGrey)"/>
      <path d="M330 0 H506 V640 Q470 900 360 1063 H0 V420 Q60 140 330 0 Z" fill="url(#frontGreen)"/>
      <path d="M506 600 Q470 880 350 1063" fill="none" stroke="var(--green-rim)" stroke-width="14"/>
      <path d="M0 522 H506 V600 Q470 880 350 1063 H0 Z" fill="url(#grass)" role="img" aria-label="Photograph of a smiling mother with her toddler sitting on sunny grass"/>
    </svg>

    <div class="brand-mark">
      <span class="brand-mark__dot"></span>
      <span class="brand-mark__name">Brightwater<br>Wellbeing<br>Rooms</span>
    </div>

    <ul class="features">
      <li><svg viewBox="0 0 26 26" aria-hidden="true"><rect x="2" y="5" width="18" height="18" fill="none" stroke="var(--sky)" stroke-width="2"/><path d="M6 13 L11 18 L23 3" fill="none" stroke="var(--sky)" stroke-width="3"/></svg>Immediate appointments</li>
      <li><svg viewBox="0 0 26 26" aria-hidden="true"><rect x="2" y="5" width="18" height="18" fill="none" stroke="var(--sky)" stroke-width="2"/><path d="M6 13 L11 18 L23 3" fill="none" stroke="var(--sky)" stroke-width="3"/></svg>After hours appointments</li>
      <li><svg viewBox="0 0 26 26" aria-hidden="true"><rect x="2" y="5" width="18" height="18" fill="none" stroke="var(--sky)" stroke-width="2"/><path d="M6 13 L11 18 L23 3" fill="none" stroke="var(--sky)" stroke-width="3"/></svg>Male and female psychologists</li>
    </ul>

    <p class="front-phone">Call us on now (03) 9563 2190</p>
    <p class="front-web">www.brightwaterwellbeingrooms.com.au</p>
  </section>

  <section class="panel panel--back">
    <svg class="panel-bg" viewBox="0 0 506 1063" preserveAspectRatio="none" aria-hidden="true">
      <defs>
        <linearGradient id="backGreen" x1="0" y1="0" x2="0.4" y2="1">
          <stop offset="0" stop-color="var(--green-mid)"/>
          <stop offset="0.5" stop-color="var(--green-pale)"/>
          <stop offset="1" stop-color="var(--green-mid)"/>
        </linearGradient>
        <linearGradient id="backGrey" x1="0" y1="0" x2="1" y2="1">
          <stop offset="0" stop-color="var(--grey-light)"/>
          <stop offset="1" stop-color="var(--grey-mid)"/>
        </linearGradient>
      </defs>
      <rect width="506" height="1063" fill="url(#backGreen)"/>
      <path d="M0 750 Q60 980 430 1063 H0 Z" fill="url(#backGrey)"/>
      <path d="M0 735 Q70 990 450 1063" fill="none" stroke="#ffffff" stroke-width="6" opacity="0.8"/>
      <path d="M0 720 Q90 1000 480 1063" fill="none" stroke="var(--green-rim)" stroke-width="8"/>
    </svg>

    <div class="services">
      <p><span class="service-title">Parenting:</span> Parenthood is an amazing journey, but for lots of people it raises all sorts of issues from fear of birth, breastfeeding difficulties and settling problems, to toddler discipline and food fussiness all the way through to getting help for your depressed or anxious adolescent. Our Parenting Psychologists can help you be the best parent you can be which will in turn lead to happier families, homes, children and parents.</p>
      <p><span class="service-title">Chronic illness/pain:</span> Diabetes, heart disease, arthritis, asthma, migraines, dizziness, chronic fatigue syndrome, infertility, and PCOS are just some of the conditions that can be managed with psychological interventions. Everything we do is about helping you to manage your condition and get back to focusing on what you really want your life to be about.</p>
      <p><span class="service-title">Eating:</span> Whether you suffer from anorexia, bulimia or binge eating, our strategies help you develop a healthy relationship with food and your body. The practical tips and strategies that we can provide are very useful for people undergoing lapband surgery or liposuction.</p>
    </div>

    <div class="brand-mark">
      <span class="brand-mark__dot"></span>
      <span class="brand-mark__name">Brightwater<br>Wellbeing<br>Rooms</span>
    </div>

    <address class="address">Suite 1, 1287 Marlowe Rd,<br>Kelverton East 3185.<br>www.brightwaterwellbeingrooms.com.au</address>

    <p class="back-phone">Call us on now (03) 9563 2190</p>
  </section>

</main>
</body>
</html>
```